Email Notification & Marketing Templates

I want to start with something like a newsletter or informational email, but i need Top Tips to Detect Phishing Scams. Something that i can send to users so they can follow it when receiving or exchanging emails. I will also need promotional items for my company that i can send to customers as well. It can be based on on our website PLVORIX.COM

Will also need:
newsletters
announcements
marketing emails
alerts
security notifications

Examples:Items such as Security Awareness Poster Series
Phishing Awareness
Password Security
Email Attachments
QR Code scams
Public WiFi safety

```html
<!DOCTYPE html>
<html lang="en">
<head>
<meta charset="utf-8">
<title>Top Tips to Detect Phishing Scams — PLVORIX</title>
<link rel="stylesheet" href="https://fonts.googleapis.com/css2?family=Montserrat:wght@600;700;800;900&family=Inter:wght@400;500&display=swap">
<style>
  :root {
    --green: #66bb1a;
    --green-soft: #e6f1dc;
    --green-mid: #b9d8a0;
    --ink: #1f1f1f;
    --body: #2e2e2e;
    --grey: #595959;
    --footer: #2b2b2b;
    --footer-deep: #1e1e1e;
    --white: #ffffff;
  }
  * { margin: 0; padding: 0; box-sizing: border-box; }
  html, body { width: 1200px; height: 4948px; overflow: hidden; background: var(--white); }
  .canvas { position: relative; width: 1200px; height: 4948px; background: var(--white); font-family: "Inter", sans-serif; color: var(--body); }
  .abs { position: absolute; }

  /* Header */
  .brand { left: 54px; top: 38px; display: flex; align-items: center; gap: 18px; font-family: "Montserrat", sans-serif; font-weight: 800; font-size: 82px; color: var(--green); letter-spacing: -1px; line-height: 1; }
  .brand-square { width: 52px; height: 52px; background: var(--green); }
  .header-pattern { left: 534px; top: 0; width: 666px; height: 207px; background: linear-gradient(135deg, #d8d8d8, #8f8f8f); }
  .hero-photo { left: 188px; top: 207px; width: 1012px; height: 626px; background: linear-gradient(135deg, #cfd2d6 0%, #9ea3a9 55%, #6b6f75 100%); }
  .hero-band { left: 534px; top: 833px; width: 666px; height: 35px; background: var(--grey); }
  .title-line { left: 0; padding-left: 67px; height: 82px; background: var(--white); font-family: "Montserrat", sans-serif; font-weight: 900; font-size: 88px; line-height: 82px; color: #3a3a3a; white-space: nowrap; }
  .title-line .hl, .title-line.hl { color: var(--green); }

  /* Tips */
  .timeline { left: 0; top: 0; }
  .illus { border-radius: 28px; background: radial-gradient(circle at 50% 55%, var(--green-mid) 0%, var(--green-soft) 60%, #f4f9ef 100%); }
  .tip { font-family: "Inter", sans-serif; }
  .tip-num { font-family: "Montserrat", sans-serif; font-weight: 700; font-size: 56px; color: var(--ink); line-height: 1; margin-bottom: 26px; }
  .tip-title { font-family: "Montserrat", sans-serif; font-weight: 700; font-size: 36px; line-height: 51px; color: var(--ink); margin-bottom: 22px; }
  .tip-title .hl { color: var(--green); }
  .tip-body { font-size: 27px; line-height: 42px; color: var(--body); }

  /* Footer */
  .footer { left: 0; top: 4458px; width: 1200px; height: 323px; background: var(--footer); }
  .footer-bottom { left: 0; top: 4781px; width: 1200px; height: 167px; background: var(--footer-deep); }
  .footer-brand { left: 67px; top: 4552px; display: flex; align-items: center; gap: 22px; font-family: "Montserrat", sans-serif; font-weight: 800; font-size: 104px; color: var(--green); line-height: 1; letter-spacing: -1px; }
  .footer-brand .brand-square { width: 62px; height: 62px; }
  .contact { color: var(--white); font-size: 28px; line-height: 42px; display: flex; gap: 18px; align-items: flex-start; }
  .contact svg { flex: none; margin-top: 8px; }
  .divider { left: 637px; top: 4637px; width: 492px; height: 2px; background: #8a8a8a; }
  .legal { left: 0; top: 4828px; width: 1200px; text-align: center; color: var(--white); font-size: 25px; }
  .legal .sep { display: inline-block; width: 2px; height: 30px; background: var(--white); vertical-align: middle; margin: 0 18px; }
</style>
</head>
<body>
<div class="canvas">

  <!-- Header -->
  <div class="abs header-pattern" role="img" aria-label="Grey geometric diamond pattern"></div>
  <div class="abs brand"><span>PLVORIX</span><span class="brand-square"></span></div>
  <div class="abs hero-photo" role="img" aria-label="Photo of a man at a laptop showing a phishing alert, with fishing hooks and envelopes floating around"></div>
  <div class="abs hero-band"></div>

  <div class="abs title-line" style="top:495px;width:495px;">TOP TIPS</div>
  <div class="abs title-line" style="top:591px;width:586px;">TO <span class="hl">DETECT</span></div>
  <div class="abs title-line hl" style="top:687px;width:534px;">PHISHING</div>
  <div class="abs title-line" style="top:783px;width:422px;">SCAMS</div>

  <!-- Timeline line -->
  <svg class="abs timeline" width="1200" height="4458" viewBox="0 0 1200 4458" aria-hidden="true">
    <polyline fill="none" stroke="#66bb1a" stroke-width="2"
      points="647,993 647,1344 570,1475 570,1834 647,1962 647,2314 570,2442 570,2803 647,2932 647,3274 570,3402 570,3773 647,3901 647,4397"/>
  </svg>

  <!-- Tip 01 -->
  <div class="abs illus" style="left:67px;top:989px;width:486px;height:355px;" role="img" aria-label="Illustration of a person at a desk checking an email on a large screen beside a mailbox"></div>
  <div class="abs tip" style="left:749px;top:990px;width:420px;">
    <div class="tip-num">01</div>
    <div class="tip-title">Check the Sender's<br><span class="hl">Email Address</span></div>
    <div class="tip-body">Look closely at the sender’s address. Attackers often use addresses that look similar to legitimate companies.</div>
  </div>

  <!-- Tip 02 -->
  <div class="abs tip" style="left:63px;top:1484px;width:460px;">
    <div class="tip-num">02</div>
    <div class="tip-title"><span class="hl">Hover Over Links</span><br>Before Clicking</div>
    <div class="tip-body">Always hover your mouse over links to see the actual destination URL before clicking.</div>
  </div>
  <div class="abs illus" style="left:682px;top:1440px;width:451px;height:413px;border-radius:50%;" role="img" aria-label="Illustration of a person leaning over a globe with a search bar and web icons"></div>

  <!-- Tip 03 -->
  <div class="abs illus" style="left:111px;top:1939px;width:392px;height:394px;border-radius:50%;" role="img" aria-label="Illustration of a person looking at a monitor showing an email with a warning sign"></div>
  <div class="abs tip" style="left:724px;top:1915px;width:450px;">
    <div class="tip-num">03</div>
    <div class="tip-title">Watch for Urgent or<br><span class="hl">Threatening Language</span></div>
    <div class="tip-body">Messages claiming your account will be locked or demanding immediate action are often phishing attempts.</div>
  </div>

  <!-- Tip 04 -->
  <div class="abs tip" style="left:63px;top:2441px;width:440px;">
    <div class="tip-num">04</div>
    <div class="tip-title"><span class="hl">Be Careful</span> with<br>Attachments</div>
    <div class="tip-body">Unexpected attachments may contain malware. If you weren't expecting it, do not open it.</div>
  </div>
  <div class="abs illus" style="left:653px;top:2423px;width:484px;height:371px;" role="img" aria-label="Illustration of a large open envelope with documents and a person sitting with a laptop"></div>

  <!-- Tip 05 -->
  <div class="abs illus" style="left:90px;top:2870px;width:419px;height:429px;" role="img" aria-label="Illustration of a person at a desk editing text on floating screens"></div>
  <div class="abs tip" style="left:730px;top:2956px;width:440px;">
    <div class="tip-num">05</div>
    <div class="tip-title">Look for <span class="hl">Spelling or<br>Grammar Errors</span></div>
    <div class="tip-body">Many phishing emails contain unusual wording or formatting.</div>
  </div>

  <!-- Tip 06 -->
  <div class="abs tip" style="left:63px;top:3418px;width:460px;">
    <div class="tip-num">06</div>
    <div class="tip-title">Never <span class="hl">Share Sensitive<br>Information</span> by Email</div>
    <div class="tip-body">Legitimate companies will never ask for passwords, banking information, or security codes through email.</div>
  </div>
  <div class="abs illus" style="left:653px;top:3398px;width:495px;height:346px;" role="img" aria-label="Illustration of a person with a tablet pointing at a blocked warning window and a lock icon"></div>

  <!-- Tip 07 -->
  <div class="abs illus" style="left:67px;top:3974px;width:505px;height:365px;" role="img" aria-label="Illustration of a phone with a security shield and login form between two people"></div>
  <div class="abs tip" style="left:718px;top:3896px;width:440px;">
    <div class="tip-num">07</div>
    <div class="tip-title"><span class="hl">Verify Requests</span><br>Through Another<br>Channel</div>
    <div class="tip-body">If an email seems suspicious, contact the organization directly using official contact details.<br>If you suspect a phishing attempt, report it immediately to your IT team.</div>
  </div>

  <!-- Footer -->
  <div class="abs footer"></div>
  <div class="abs footer-brand"><span>PLVORIX</span><span class="brand-square"></span></div>

  <div class="abs contact" style="left:644px;top:4516px;">
    <svg width="24" height="30" viewBox="0 0 24 30" aria-hidden="true"><path d="M12 0C5.4 0 0 5.2 0 11.7 0 20 12 30 12 30s12-10 12-18.3C24 5.2 18.6 0 12 0z" fill="#ffffff"/><circle cx="12" cy="11.5" r="4.5" fill="#2b2b2b"/></svg>
    <div>418 Linden Ridge Ave.<br>Suite 3 &amp; 4, Brookfield, OH 44512</div>
  </div>
  <div class="abs divider"></div>
  <div class="abs contact" style="left:644px;top:4667px;">
    <svg width="26" height="26" viewBox="0 0 24 24" aria-hidden="true"><path d="M6.6 10.8a15.1 15.1 0 0 0 6.6 6.6l2.2-2.2c.3-.3.7-.4 1-.2 1.1.4 2.3.6 3.6.6.6 0 1 .4 1 1V20c0 .6-.4 1-1 1A17 17 0 0 1 3 4c0-.6.4-1 1-1h3.5c.6 0 1 .4 1 1 0 1.2.2 2.4.6 3.6.1.3 0 .7-.2 1z" fill="#ffffff"/></svg>
    <div>(555) 318-4720</div>
  </div>

  <div class="abs footer-bottom"></div>
  <div class="abs legal">Unsubscribe<span class="sep"></span>Copyright © 2026 All Rights Reserved</div>

</div>
</body>
</html>
```